Gaming company needs web presence

PLEASE NOTE: We need just a simple web site. We are at least a year away from launching our first product, so the site only needs a small amount of information on it. The only people who will be visiting the web site are prospective employees, prospective investors who want a little information on the company, journalists who want a little more information, and people in the games industry who will visit to read blog posts about the development of our first game.

Brindlewick Games is a new gaming company that wants to change how people think about video games. We are making games that we think can be so interesting to watch that people might want to tune into them instead of the TV.

The games we make are sophisticated, they are not for children, and we want to project an image of being serious about our craft and the brand we're trying to create. Our games are heavily focused on players interacting with each other in sophisticated ways: to negotiate, to compete, to fight, to come to each other's rescue, to cheer each other on, or to simply watch each other in awe.

We do not want a site that features lots of video game cliches like joysticks, 8 bit graphics, science fiction themes, or military themes. We are focused on craftsmanship, so we'd like to project a sense of precision, pride and deep purpose.

The purpose of this website is to create an image of our company that can help us recruit like-minded craftspeople and help find business partners. There will be no e-commerce, account creation, or forums for some time. The site should have:
-A front page that describes our business
-A section that describes our first game (we have only one for now)
-A section for employees to write blog posts. There should be something on the home page that shows links to the latest 3 blog posts.
-A section about founders that shows information about them.
-Contact information, lets people send us email

Our first game is one that looks very realistic. It takes place on a tropical island. We can't say a lot more about it in public yet, but I will say these things: it is not a game that children will play, it is not very violent, it would look more like a film than a typical video game.

And the site should be easily extendable when we have more content and more categories of content.

I've attached our official company logo with a color scheme we've been using, plus an alternate version of the logo. Please use this as a starting point for the web site's visual design. Also, I do not think it is necessary to use the dark background in the logo as the background throughout the site. I wouldn't rule it out, but I'd like to see some proposals with lighter backgrounds.

We need to be able to get code from you so that we can drop it on our server and get it running without extra effort. We need to be able to add content for Blog posts easily as well, so please indicate how that would work.
Updates

Hello everyone, Thanks for all of the great submissions so far. There are some important things I'd like to relay to everyone: We are at least a year away from launching our first game, so we only need a simple web site. Unfortunately, we can't share any screenshots or details about our first game yet. All of these submissions look great, but are far too complicated. Also, I really want to stress that we don't want to feature stock photography of people playing games, especially of children playing games. In fact, since we don't want to release any screenshots of our games and we don't have any good photography of ourselves working, it's best if there are no photographic images on the site for now.

Hello designers, Can you let me know if your designs include all the code that would let us drop the files on to our web server and easily get it up and running? Also, can you tell me how the blog posts would be created? Does your code run on a CMS? Thanks, Hollis

Hi Designers, we will be hosting this site with Wordpress, so we would prefer to have submissions ready to go on a Wordpress server. Thanks!

Target Market(s)

Investors, prospective employees, press, blog post readers.

Industry/Entity Type

Business

Font styles to use
Sans Serif

Requirements
Must have
• Simplicity first. Please use a color palette and fonts that match our logo.
Should not have
• Video game cliches. Flash animations or menus.
No children.
No photographs of people playing games.

(I realize this is very limiting, but we're keeping the sits as simple as possible for now)

```html
<!DOCTYPE html>
<html lang="en">
<head>
<meta charset="utf-8">
<title>Brindlewick Games</title>
<link rel="stylesheet" href="https://fonts.googleapis.com/css2?family=Alfa+Slab+One&family=Cabin:wght@400;500;600&family=Ubuntu:wght@300;400;500&display=swap">
<style>
:root{
  --brown-dark:#3f1f0d;
  --brown:#5a2e14;
  --brown-mid:#6e3a1b;
  --orange:#c8773a;
  --orange-soft:#d98d4c;
  --cream:#fbf8e4;
  --cream-text:#eadfc4;
  --white:#ffffff;
  --text:#4a2511;
  --muted:#8a8a8a;
  --line:#e2ddd0;
}
*{box-sizing:border-box;margin:0;padding:0}
html,body{width:672px;height:1200px;overflow:hidden}
body{position:relative;background:var(--white);font-family:"Ubuntu",sans-serif;color:var(--text)}
.abs{position:absolute}

/* header */
.hero{left:0;top:0;width:672px;height:305px;background:linear-gradient(180deg,var(--brown-mid) 0%,var(--brown) 55%,#4d260f 100%)}
.brand{left:82px;top:36px;font-family:"Cabin",sans-serif;font-weight:600;font-size:19px;color:var(--white);letter-spacing:.5px;line-height:1}
.brand-sub{display:block;font-size:10px;letter-spacing:3px;margin-top:6px;text-align:center}
.social{right:74px;top:24px;display:flex;gap:3px}
.social span{width:10px;height:10px;border-radius:50%;background:var(--cream-text)}
.nav{left:292px;top:53px;display:flex;gap:0;font-family:"Ubuntu",sans-serif;font-size:8px;color:var(--white);letter-spacing:.2px}
.nav a{color:inherit;text-decoration:none;position:absolute;white-space:nowrap}
.tagline{font-family:"Alfa Slab One",serif;font-size:21px;letter-spacing:1.5px;line-height:25px;white-space:nowrap}
.tagline .light{color:var(--cream-text)}
.tagline .accent{color:var(--orange-soft)}
.tag-left{left:103px;top:166px}
.tag-right{left:388px;top:166px}
.hero-badge{left:273px;top:131px;width:102px;height:102px;border-radius:50%;background:var(--orange)}
.hero-rule{top:255px;height:1px;background:var(--orange)}
.hero-dot{top:252px;width:6px;height:6px;background:var(--orange);transform:rotate(45deg)}
.pointer{left:310px;top:304px;width:0;height:0;border-left:22px solid transparent;border-right:22px solid transparent;border-top:24px solid #4d260f}

/* process */
.process{left:0;top:305px;width:672px;height:120px;background:var(--cream)}
.step{width:90px;text-align:center;font-size:9px;letter-spacing:.3px;color:var(--text)}
.step svg{display:block;margin:0 auto 6px}
.plus{font-size:12px;color:var(--orange);font-weight:300}

/* welcome */
h2{font-family:"Cabin",sans-serif;font-weight:400;color:var(--text);text-align:center}
.welcome-title{left:0;top:439px;width:672px;font-size:16px}
.copy{font-size:6px;line-height:9.5px;color:var(--muted);text-align:center}
.welcome-copy{left:110px;top:464px;width:452px}
.welcome-copy p+p{margin-top:9px}

/* founders */
.founders-title{left:0;top:547px;width:672px;font-size:18px}
.founder{width:110px;text-align:center;top:578px}
.portrait{width:108px;height:108px;border-radius:50%;border:3px solid #efefef;background:radial-gradient(circle at 50% 40%,#cfcfcf 0%,#9a9a9a 55%,#e8e8e8 100%);margin:0 auto}
.founder-name{margin-top:8px;font-size:9px;letter-spacing:.4px;color:var(--text)}
.founder-role{margin-top:4px;font-size:5.5px;color:var(--orange);letter-spacing:.3px}
.read-more{display:inline-block;margin-top:7px;background:var(--brown-dark);color:var(--white);font-size:6px;padding:3px 7px;letter-spacing:.3px}

/* games + blog */
.section-head{font-family:"Cabin",sans-serif;font-size:11px;letter-spacing:.4px;color:var(--text);border-bottom:1px solid var(--orange);padding-bottom:5px}
.games-head{left:97px;top:797px;width:308px}
.blog-head{left:432px;top:797px;width:148px}
.games-art{left:110px;top:830px;width:280px;height:166px;background:linear-gradient(180deg,#f3efe8 0%,#e3cbb3 60%,#d7b497 100%)}
.games-screen{left:190px;top:855px;width:114px;height:62px;background:var(--white);border:5px solid #222;text-align:center;font-family:"Cabin",sans-serif;color:#222;padding-top:8px}
.games-screen b{display:block;font-weight:400;font-size:10px;line-height:12px}
.games-screen small{display:block;font-size:7px;margin-top:2px}
.post{left:436px;width:145px}
.post-thumb{position:absolute;left:0;top:0;width:61px;height:36px;background:linear-gradient(135deg,#3a2a5a 0%,#b4425a 55%,#e0a070 100%)}
.post-thumb.alt{background:linear-gradient(135deg,#d8b58a 0%,#8a4a2a 55%,#3a2418 100%)}
.post-title{position:absolute;left:67px;top:2px;font-size:6px;font-weight:500;color:var(--orange)}
.post-meta{position:absolute;left:67px;font-size:5.5px;color:var(--muted);display:flex;align-items:center;gap:3px}
.post-meta i{width:5px;height:5px;border-radius:50%;border:1px solid var(--brown-dark);display:inline-block}
.post-excerpt{position:absolute;left:0;top:39px;width:145px;font-size:5.5px;line-height:7.5px;color:#9a9a9a}
.post-rule{left:436px;top:899px;width:144px;border-top:1px dotted #c9c2b4}

/* contact */
.contact{left:0;top:996px;width:672px;height:161px;background:var(--cream)}
.contact-title{left:0;top:1008px;width:672px;font-size:15px}
.contact-copy{left:110px;top:1033px;width:452px}
.field{background:var(--white);border:1px solid #ece6d2;font-size:6.5px;color:var(--muted);padding:4px 8px}
.send{left:336px;top:1114px;width:220px;height:18px;background:var(--brown-dark);color:var(--orange-soft);font-size:8px;letter-spacing:1.5px;text-align:center;line-height:18px;font-weight:500}

/* footer */
.footer{left:0;top:1157px;width:672px;height:43px;background:var(--brown-dark)}
.footer-brand{left:96px;top:1165px;font-family:"Cabin",sans-serif;font-weight:600;font-size:17px;color:var(--white);line-height:1;text-align:center}
.footer-brand span{display:block;font-size:8px;letter-spacing:3px;margin-top:4px}
.legal{left:368px;top:1176px;font-size:6px;color:var(--cream-text)}
.footer-social{left:512px;top:1175px;display:flex;gap:9px}
.footer-social span{width:9px;height:9px;border-radius:50%;background:var(--cream-text)}
</style>
</head>
<body>

<!-- header -->
<header class="abs hero"></header>
<div class="abs brand">BRINDLEWICK<span class="brand-sub">GAMES</span></div>
<div class="abs social"><span></span><span></span><span></span><span></span></div>
<nav class="abs nav" style="left:0;top:53px;width:672px;height:12px">
  <a style="left:292px">HOME</a>
  <a style="left:337px">ABOUT US</a>
  <a style="left:397px">SERVICES</a>
  <a style="left:455px">BLOG</a>
  <a style="left:498px">REVIEWS</a>
  <a style="left:553px">CONTACT US</a>
</nav>
<div class="abs tagline tag-left"><div class="light">THE WORLD</div><div class="accent">YOUR SKILL</div></div>
<div class="abs hero-badge"></div>
<div class="abs tagline tag-right"><div class="light">WANTS TO SEE</div><div class="accent">&amp; CREATIVITY</div></div>
<div class="abs hero-rule" style="left:182px;width:124px"></div>
<div class="abs hero-dot" style="left:324px"></div>
<div class="abs hero-dot" style="left:333px"></div>
<div class="abs hero-rule" style="left:350px;width:124px"></div>
<div class="abs pointer"></div>

<!-- process -->
<section class="abs process"></section>
<div class="abs step" style="left:74px;top:337px">
  <svg width="30" height="40" viewBox="0 0 30 40" fill="none" stroke="#c8773a" stroke-width="1.3"><path d="M15 2a11 11 0 0 0-6 20v6h12v-6A11 11 0 0 0 15 2z"/><path d="M10 32h10M11 36h8M12 22l3-6 3 6"/></svg>DISCOVER</div>
<div class="abs plus" style="left:187px;top:352px">+</div>
<div class="abs step" style="left:216px;top:337px">
  <svg width="40" height="40" viewBox="0 0 40 40" fill="none" stroke="#c8773a" stroke-width="1.3"><path d="M6 34l4-10L30 4l6 6-20 20z"/><path d="M34 34l-4-10L10 4 4 10l20 20z"/></svg>DESIGN</div>
<div class="abs plus" style="left:329px;top:352px">+</div>
<div class="abs step" style="left:359px;top:337px">
  <svg width="44" height="40" viewBox="0 0 44 40" fill="none" stroke="#c8773a" stroke-width="1.3"><rect x="2" y="3" width="40" height="26" rx="1"/><path d="M16 29v6h12v-6M12 37h20"/></svg>DEVELOP</div>
<div class="abs plus" style="left:471px;top:352px">+</div>
<div class="abs step" style="left:499px;top:337px">
  <svg width="40" height="40" viewBox="0 0 40 40" fill="none" stroke="#c8773a" stroke-width="1.3"><path d="M36 4L20 12 8 28l4 4 16-12z"/><path d="M14 14l-8 2 4 6M26 26l-2 8-6-4M8 34l4-4"/></svg>DEPLOY</div>

<!-- welcome -->
<h2 class="abs welcome-title">WELCOME TO BRINDLEWICK GAMES</h2>
<div class="abs copy welcome-copy">
  <p>We build games made with care, patience and a deep respect for the craft. Every system, scene and sound is shaped by a small team that values precision over noise. Our players meet, bargain, compete and rescue each other in worlds designed to be as good to watch as they are to play. We are hiring thoughtful people.</p>
  <p>Our first title is in development now, and we will share more about it here when the time is right.</p>
</div>

<!-- founders -->
<h2 class="abs founders-title">FOUNDERS</h2>
<div class="abs founder" style="left:103px"><div class="portrait" role="img" aria-label="Portrait of Mirabel Ashcombe"></div><div class="founder-name">MIRABEL ASHCOMBE</div><div class="founder-role">NON EXECUTIVE CHAIRMAN</div><span class="read-more">READ MORE</span></div>
<div class="abs founder" style="left:225px"><div class="portrait" role="img" aria-label="Portrait of Gerald Finchley"></div><div class="founder-name">GERALD FINCHLEY</div><div class="founder-role">NON EXECUTIVE CHAIRMAN</div><span class="read-more">READ MORE</span></div>
<div class="abs founder" style="left:346px"><div class="portrait" role="img" aria-label="Portrait of Oswin Parrish"></div><div class="founder-name">OSWIN PARRISH</div><div class="founder-role">MANAGING DIRECTOR</div><span class="read-more">READ MORE</span></div>
<div class="abs founder" style="left:467px"><div class="portrait" role="img" aria-label="Portrait of Tobias Okonedo"></div><div class="founder-name">TOBIAS OKONEDO</div><div class="founder-role">GAME DEV DIRECTOR</div><span class="read-more">READ MORE</span></div>

<!-- upcoming games -->
<div class="abs section-head games-head">UPCOMING GAMES</div>
<div class="abs games-art" role="img" aria-label="Two hands holding a phone sideways"></div>
<div class="abs games-screen"><b>UNDER<br>DEVELOPMENT</b><small>DETAILS COMING SOON</small></div>

<!-- recent blogs -->
<div class="abs section-head blog-head">RECENT BLOGS</div>
<article class="abs post" style="top:832px;height:60px">
  <div class="post-thumb" role="img" aria-label="Blog post artwork"></div>
  <div class="post-title">LACUS LEO FERMENT</div>
  <div class="post-meta" style="top:14px"><i></i>05 Hours ago</div>
  <div class="post-meta" style="top:24px"><i></i>20 comments</div>
  <p class="post-excerpt">A first look at how our small team plans each week of work on the island.</p>
</article>
<div class="abs post-rule"></div>
<article class="abs post" style="top:909px;height:80px">
  <div class="post-thumb alt" role="img" aria-label="Blog post artwork"></div>
  <div class="post-title">LACUS LEO FERMENT</div>
  <div class="post-meta" style="top:14px"><i></i>05 Hours ago</div>
  <div class="post-meta" style="top:24px"><i></i>20 comments</div>
  <p class="post-excerpt">Notes on sound, light and pacing from the latest studio review session.</p>
</article>

<!-- contact -->
<section class="abs contact"></section>
<h2 class="abs contact-title">CONTACT US</h2>
<p class="abs copy contact-copy">If you would like to reach us or ask a question, you can do so through this form. We will get back to you as soon as possible.</p>
<div class="abs field" style="left:113px;top:1066px;width:216px;height:16px">Name</div>
<div class="abs field" style="left:113px;top:1090px;width:216px;height:16px">Email Address</div>
<div class="abs field" style="left:113px;top:1115px;width:216px;height:16px">Inquiry Reason</div>
<div class="abs field" style="left:338px;top:1066px;width:216px;height:40px">Contact Number</div>
<div class="abs send">SEND</div>

<!-- footer -->
<footer class="abs footer"></footer>
<div class="abs footer-brand">BRINDLEWICK<span>GAMES</span></div>
<div class="abs legal">© 2014 All Rights Reserved &nbsp;|&nbsp; Privacy Policy</div>
<div class="abs footer-social"><span></span><span></span><span></span><span></span></div>

</body>
</html>
```